Harbourline Strategy Group firm

I need a business card that is succint for a Brisbane based business called Harbourline Strategy Group Pty Ltd.
We bridge the gaps between People, Process and Technology.

We are a specialist operational excellence firm, delivering strategic consulting and business advisory services in six core capabilities, across all industries and all business lines to improve performance, efficiency, profitability, automation and scalability, for clients across Australia &New Zealand.
Updates

Hi Designers, I have uploaded the logo in 3D .png format, to assist in card design.

Target Market(s)

Project Management professionals, IT professionals, corporate and government clients managing transitioning or transformation projects.

Contact Information for Business Card

Harbourline Strategy Group Pty Ltd

Daniel Ferreira
Principal Consultant

mobile: +61 417 260 315
email: daniel@harbourlinestrategygroup.com.au
webpage: www.harbourlinestrategygroup.com

professional services: strategic advisors,

Font styles to use
Sans Serif

Requirements
Must have
• Business name: Harbourline Strategy Group
logo: attached
Contact person: Daniel Ferreira
Title: Principal Consultant
contact details:
mobile +61 417 260
email: daniel@HarbourlineStrategyGroup.com.au
website: HarbourlineStrategyGroup.com

on back side with logo include: A.B.N. 58210947362

professional services offered: Business Analysis, Strategic Advisory
Nice to have
• QR code
Should not have
• contacts picture

```html
<!DOCTYPE html>
<html lang="en">
<head>
<meta charset="utf-8">
<title>Harbourline Strategy Group – Business Card</title>
<link href="https://fonts.googleapis.com/css2?family=Poppins:wght@400;500;700&display=swap" rel="stylesheet">
<style>
  :root {
    --navy: #262e5f;
    --navy-soft: #313a6e;
    --red: #d3252e;
    --white: #ffffff;
    --paper: #f2f2f2;
    --stage: #e7e4df;
    --ink: #2b2f55;
  }
  * { box-sizing: border-box; margin: 0; padding: 0; }
  html, body { width: 1200px; height: 780px; overflow: hidden; }
  body {
    background: var(--stage);
    font-family: "Poppins", Arial, sans-serif;
    display: flex;
    align-items: center;
    justify-content: center;
    gap: 40px;
  }
  .card {
    position: relative;
    width: 540px;
    height: 310px;
    border-radius: 4px;
    overflow: hidden;
    box-shadow: 0 10px 28px rgba(0,0,0,0.22);
  }
  .card-shapes { position: absolute; inset: 0; }

  /* Front */
  .front-brand {
    position: absolute;
    top: 46px;
    right: 120px;
    width: 220px;
    text-align: right;
    color: var(--navy);
    font-weight: 700;
    font-size: 26px;
    line-height: 1.05;
    text-transform: uppercase;
    letter-spacing: 0.5px;
  }
  .contact-block {
    position: absolute;
    left: 78px;
    bottom: 42px;
  }
  .person-name {
    color: var(--navy);
    font-weight: 700;
    font-size: 17px;
    text-transform: uppercase;
    letter-spacing: 0.3px;
  }
  .person-title {
    color: var(--red);
    font-size: 12.5px;
    margin-bottom: 14px;
  }
  .contact-list { list-style: none; }
  .contact-list li {
    display: flex;
    align-items: center;
    gap: 8px;
    color: var(--ink);
    font-size: 11.5px;
    line-height: 20px;
  }
  .contact-icon { width: 14px; height: 14px; flex: none; }

  /* Back */
  .back { background: var(--navy); }
  .world-map {
    position: absolute;
    inset: 30px 40px;
    border-radius: 40% 45% 38% 42%;
    background: radial-gradient(ellipse at center, var(--navy-soft) 0%, rgba(49,58,110,0.4) 60%, rgba(38,46,95,0) 100%);
  }
  .back-brand {
    position: absolute;
    top: 92px;
    right: 56px;
    width: 270px;
    text-align: right;
    color: var(--white);
    font-weight: 700;
    font-size: 30px;
    line-height: 1.05;
    text-transform: uppercase;
    letter-spacing: 0.5px;
  }
  .back-details {
    position: absolute;
    left: 40px;
    top: 36px;
    color: var(--white);
    font-size: 12px;
    line-height: 22px;
    letter-spacing: 0.4px;
  }
</style>
</head>
<body>

  <section class="card front" aria-label="Business card front">
    <svg class="card-shapes" viewBox="0 0 540 310" preserveAspectRatio="none" aria-hidden="true">
      <rect width="540" height="310" fill="var(--red)"/>
      <path d="M0,0 L60,0 Q20,150 120,310 L0,310 Z" fill="var(--navy)"/>
      <path d="M60,0 L400,0 Q530,150 430,310 L120,310 Q20,150 60,0 Z" fill="var(--paper)"/>
    </svg>

    <div class="front-brand">Harbourline Strategy Group</div>

    <div class="contact-block">
      <p class="person-name">Daniel Ferreira</p>
      <p class="person-title">Principal Consultant</p>
      <ul class="contact-list">
        <li>
          <svg class="contact-icon" viewBox="0 0 14 14" aria-hidden="true"><circle cx="7" cy="7" r="6.3" fill="none" stroke="var(--red)" stroke-width="1.2"/><rect x="4.8" y="3.5" width="4.4" height="7" rx="0.8" fill="var(--red)"/></svg>
          +61 417 260
        </li>
        <li>
          <svg class="contact-icon" viewBox="0 0 14 14" aria-hidden="true"><circle cx="7" cy="7" r="6.3" fill="none" stroke="var(--red)" stroke-width="1.2"/><rect x="3.8" y="4.6" width="6.4" height="4.8" fill="var(--red)"/><path d="M3.8,4.6 L7,7.3 L10.2,4.6" fill="none" stroke="var(--white)" stroke-width="0.8"/></svg>
          daniel@HarbourlineStrategyGroup.com.au
        </li>
        <li>
          <svg class="contact-icon" viewBox="0 0 14 14" aria-hidden="true"><circle cx="7" cy="7" r="6.3" fill="none" stroke="var(--red)" stroke-width="1.2"/><circle cx="7" cy="7" r="3.4" fill="none" stroke="var(--red)" stroke-width="1"/><path d="M3.6,7 H10.4 M7,3.6 V10.4" stroke="var(--red)" stroke-width="0.8"/></svg>
          HarbourlineStrategyGroup.com
        </li>
      </ul>
    </div>
  </section>

  <section class="card back" aria-label="Business card back">
    <div class="world-map" role="img" aria-label="Faint world map backdrop"></div>
    <div class="back-details">
      <p>Business Analysis | Strategic Advisory</p>
      <p>A.B.N. 58210947362</p>
    </div>
    <div class="back-brand">Harbourline Strategy Group Pty Ltd</div>
  </section>

</body>
</html>
```